A fresh look at Kelmorra website

We are looking to freshen the design of our website. As part of the changes, we would like to make the design more gender-neutral and incorporate the 5 main industries. We would like to have a landing page for each industry and a CTA on the home page to direct the traffic to the specific industry. We are a B2B business that supplies in Australia Mainly to Victoria, consumables for the Food Processing Industry, Industry ( mechanics, manufacturing and businesses that require personal protective equipment), Childcare, Aged care and Education) We are looking to make the landing pages as specific to the five sectors as we can only displaying relevant information for that industry. our goal is to make the design as intuitive as possible making it easy and inviting for the end-user. the current site at www.kelmorra.com.au

Target Market(s)

Childcare, Industry, Food Processing Industry, Aged care, Education. All B2B markets

Number of Pages Required

5+ page

Font styles to use
Sans Serif

Colors

Designer to choose colors to be used in the design.

Requirements
Must have
• follow our brand briefing colours and fonts, A local feel for Victoria Australia.
• have all the components in the header that are currently on the website.
• have a add to quote button and have the selections for products where needed Eg size quantitiy ect
Should not have
• Global Imagery

```html
<!DOCTYPE html>
<html lang="en">
<head>
<meta charset="utf-8">
<title>Kelmorra – Hygiene & Safety Supplies</title>
<link href="https://fonts.googleapis.com/css2?family=Montserrat:wght@500;600;700;800&family=Open+Sans:wght@400;600;700&display=swap" rel="stylesheet">
<style>
:root{
  --green:#6aae3c;
  --green-dark:#4f8d27;
  --ink:#2b2f33;
  --muted:#7b8087;
  --line:#e3e6e9;
  --bg:#f3f4f5;
  --white:#ffffff;
  --charcoal:#2f3338;
  --red:#e2412f;
  --blue:#2f79c4;
}
*{box-sizing:border-box;margin:0;padding:0}
html,body{width:1200px;height:3324px;overflow:hidden}
body{font-family:"Open Sans",Arial,sans-serif;color:var(--ink);background:var(--white);position:relative;font-size:13px}
h1,h2,h3,h4,.brand{font-family:"Montserrat",Arial,sans-serif}
.abs{position:absolute}

/* header */
.topstrip{top:0;left:0;width:1200px;height:32px;border-bottom:1px solid var(--line);font-size:11px;color:var(--muted)}
.topstrip span{position:absolute;top:9px}
.site-header{top:32px;left:0;width:1200px;height:80px;border-bottom:1px solid var(--line)}
.brand{position:absolute;left:72px;top:22px;font-size:30px;font-weight:800;color:var(--green);letter-spacing:1px;display:flex;align-items:center;gap:10px}
.brand i{width:18px;height:18px;border-radius:50%;background:var(--green);display:block}
.shop-toggle{position:absolute;left:316px;top:26px;display:flex;align-items:center;gap:10px;font-size:11px;font-weight:600;white-space:nowrap}
.pill{background:var(--green);color:#fff;padding:7px 14px;border-radius:16px}
.switch{width:36px;height:18px;border-radius:9px;background:var(--charcoal);position:relative}
.switch:after{content:"";position:absolute;right:3px;top:3px;width:12px;height:12px;border-radius:50%;background:#fff}
.search{position:absolute;left:650px;top:22px;width:270px;height:36px;border:1px solid var(--line);border-radius:18px;padding:9px 18px;color:var(--muted);font-size:12px;white-space:nowrap}
.header-icons{position:absolute;left:940px;top:24px;display:flex;gap:14px;align-items:center}
.login{border:1px solid var(--green);color:var(--green);border-radius:16px;padding:6px 14px;font-size:12px;font-weight:600}
.icon-btn{width:32px;height:32px;border-radius:50%;border:1px solid var(--line);display:flex;align-items:center;justify-content:center}

/* hero */
.hero-main{top:128px;left:72px;width:780px;height:424px;background:linear-gradient(120deg,#1e3e6b,#3f6fa6 55%,#9bb9d6);color:#fff}
.hero-main .txt{position:absolute;left:60px;top:90px}
.hero-main small{font-size:13px;letter-spacing:2px;font-weight:600}
.hero-main h1{font-size:50px;font-weight:800;line-height:1.1;margin:8px 0}
.hero-main p{font-size:16px}
.btn{display:inline-block;border-radius:18px;padding:9px 22px;font-size:12px;font-weight:600;font-family:"Montserrat",sans-serif;white-space:nowrap}
.btn-green{background:var(--green);color:#fff}
.btn-white{background:#fff;color:var(--ink);border:1px solid var(--line)}
.btn-outline{border:1px solid var(--green);color:var(--green);background:#fff}
.hero-main .btn{margin-top:22px}
.promo{left:888px;width:240px;height:200px}
.promo h3{position:absolute;left:18px;top:20px;font-size:22px;font-weight:700}
.promo p{position:absolute;left:18px;top:52px;font-size:12px}
.promo .btn{position:absolute;left:18px;top:80px;padding:6px 14px;font-size:11px}
.promo-clear{top:128px;background:linear-gradient(135deg,#3a3f46,#5d646c);color:#fff}
.promo-drop{top:352px;background:#eef0ea;color:var(--green-dark)}

/* industry */
.industry{top:572px;left:72px;width:1056px;height:348px;background:#fff;box-shadow:0 4px 20px rgba(0,0,0,.08);text-align:center}
.industry h2{font-size:28px;font-weight:700;margin-top:36px}
.industry h2+i{display:block;width:50px;height:3px;background:var(--green);margin:12px auto 0}
.ind-row{display:flex;justify-content:space-around;padding:0 60px;margin-top:40px}
.ind{width:150px;font-size:14px;font-weight:600;font-family:"Montserrat",sans-serif}
.ind svg{display:block;margin:0 auto 14px}
.ind.active span{border-bottom:2px solid var(--green);padding-bottom:4px}
.industry .btn{margin-top:40px}

/* sidebar */
.sidebar{top:940px;left:72px;width:240px}
.side-head{background:var(--green);color:#fff;font-family:"Montserrat",sans-serif;font-weight:700;font-size:13px;padding:12px 16px}
.cat-list{list-style:none;border:1px solid var(--line);border-top:none}
.cat-list li{height:36px;line-height:36px;padding:0 16px;border-bottom:1px solid var(--line);font-size:12px;display:flex;justify-content:space-between}
.cat-list li:after{content:"›";color:var(--muted)}
.cat-list li.on{background:var(--bg);font-weight:600}
.guide{margin-top:20px;height:160px;background:#eef3e8;padding:24px 18px;position:relative}
.guide h4{font-size:21px;font-weight:800;color:var(--green);line-height:1}
.guide p{font-size:11px;font-weight:700;margin-top:6px}
.guide .btn{margin-top:16px;padding:6px 14px;font-size:11px}
.guide .cover{position:absolute;right:14px;top:34px;width:56px;height:92px;background:linear-gradient(#8dc360,#4f8d27)}

/* products */
.products{top:940px;left:344px;width:784px}
.prod-head{height:40px;background:var(--green);color:#fff;font-family:"Montserrat",sans-serif;font-weight:700;font-size:13px;text-align:center;line-height:40px;letter-spacing:.5px}
.grid{display:grid;grid-template-columns:repeat(3,240px);gap:32px 32px;margin-top:24px}
.card{height:384px;border:1px solid var(--line);background:#fff;position:relative;padding:16px}
.card.lift{box-shadow:0 6px 22px rgba(0,0,0,.12)}
.thumb{height:170px;background:linear-gradient(135deg,#dfe7ef,#b9cbdd);border-radius:2px}
.thumb.alt{background:linear-gradient(135deg,#f0f3f5,#cfd8e0)}
.badge{position:absolute;right:12px;top:12px;width:40px;height:40px;border-radius:50%;color:#fff;font-size:10px;font-weight:700;text-align:center;line-height:40px}
.badge.sale{background:var(--red)}
.badge.new{background:var(--blue)}
.card h3{font-size:13px;font-weight:700;margin-top:16px;line-height:1.4}
.price{margin-top:8px;font-size:11px;color:var(--muted)}
.price s{margin-right:4px}
.price b{color:var(--green);font-size:15px}
.opts{display:flex;gap:8px;margin-top:12px;align-items:center;font-size:11px;color:var(--muted)}
.qty{border:1px solid var(--line);border-radius:12px;padding:3px 10px}
.stock{color:var(--green)}
.actions{position:absolute;left:16px;bottom:18px;display:flex;gap:8px}
.actions .btn{padding:7px 14px;font-size:11px}

/* suppliers */
.suppliers{top:1880px;left:0;width:1200px;height:120px;background:var(--charcoal)}
.sup-tag{position:absolute;left:0;top:0;height:120px;width:330px;background:#24282c}
.sup-tag svg{position:absolute;left:300px;top:0}
.sup-tag h2{position:absolute;left:72px;top:44px;color:#fff;font-size:24px;font-weight:700}
.sup-logos{position:absolute;left:400px;top:34px;width:760px;height:52px;background:#fff;display:flex;justify-content:space-around;align-items:center}
.sup-logos span{font-family:"Montserrat",sans-serif;font-weight:700;font-size:22px;color:var(--ink)}

/* testimonial */
.clients{top:2040px;left:72px;width:1056px;height:460px;background:var(--green);color:#fff;text-align:center}
.clients h2{font-size:28px;font-weight:700;margin-top:34px}
.clients h2+i{display:block;width:50px;height:3px;background:#fff;margin:12px auto 0}
.quote-card{width:800px;height:280px;margin:30px auto 0;background:#fff;color:var(--ink);padding:28px 80px}
.quote-mark{font-family:"Montserrat",sans-serif;font-size:48px;font-weight:800;color:var(--green);line-height:1}
.quote-card p{font-size:13px;line-height:1.8;margin-top:10px;color:var(--muted)}
.quote-card .who{margin-top:16px;font-size:12px}
.quote-card .who b{color:var(--ink)}

/* news */
.news{top:2560px;left:72px;width:1056px;text-align:center}
.news h2{font-size:32px;font-weight:700}
.news h2+i{display:block;width:50px;height:3px;background:var(--green);margin:12px auto 0}
.news-grid{display:grid;grid-template-columns:repeat(3,1fr);gap:24px;margin-top:34px;text-align:center}
.news-img{height:184px}
.n1{background:linear-gradient(135deg,#d5d9de,#8b96a3)}
.n2{background:linear-gradient(135deg,#3f8fd0,#9cc4e6)}
.n3{background:linear-gradient(135deg,#7a8794,#c9d0d6)}
.news-card .cat{color:var(--green);font-size:11px;font-weight:700;letter-spacing:1px;margin-top:18px}
.news-card h3{font-size:18px;font-weight:700;line-height:1.35;margin:10px 20px 0}
.news .btn{margin-top:36px}

/* footer */
.site-footer{top:3064px;left:0;width:1200px;height:260px;background:var(--charcoal);color:#c4c8cc;font-size:12px}
.fcol{position:absolute;top:32px}
.fcol h4{color:#fff;font-size:14px;font-weight:700;margin-bottom:14px}
.fcol p{line-height:1.7}
.subscribe{display:flex;margin-top:14px}
.subscribe span{width:180px;height:32px;border:1px solid #555b61;padding:7px 10px;color:#8d9298}
.subscribe b{background:var(--green);color:#fff;padding:8px 14px;font-size:11px}
.socials{display:flex;gap:8px;margin-top:14px}
.socials i{width:26px;height:26px;border-radius:50%;background:#4a5056;display:block}
.links{display:grid;grid-template-columns:120px 120px;gap:6px 20px}
.contact li{list-style:none;display:flex;gap:8px;align-items:center;margin-bottom:6px}
.copy{position:absolute;left:72px;right:72px;bottom:0;height:40px;border-top:1px solid #454a50;display:flex;justify-content:space-between;align-items:center;font-size:11px;color:#8d9298}
</style>
</head>
<body>

<div class="abs topstrip">
  <span style="left:72px">1800 555 214</span>
  <span style="left:180px">sales@kelmorra.com.au</span>
  <span style="left:920px">Track Order</span>
  <span style="left:1010px">Help Centre</span>
</div>

<header class="abs site-header">
  <div class="brand"><i></i>KELMORRA</div>
  <div class="shop-toggle">
    <span class="pill">Shop by Standard</span>
    <span class="switch"></span>
    <span class="pill">Shop by Industry</span>
  </div>
  <div class="search">Search products...</div>
  <div class="header-icons">
    <div class="icon-btn"><svg width="14" height="14" viewBox="0 0 14 14" fill="none" stroke="#7b8087" stroke-width="1.5"><path d="M7 12s-5-3-5-7a3 3 0 0 1 5-2 3 3 0 0 1 5 2c0 4-5 7-5 7z"/></svg></div>
    <span class="login">Login</span>
    <div class="icon-btn"><svg width="16" height="16" viewBox="0 0 16 16" fill="none" stroke="#2b2f33" stroke-width="1.5"><path d="M1 2h2l2 9h8l2-6H4"/><circle cx="6" cy="14" r="1"/><circle cx="12" cy="14" r="1"/></svg></div>
  </div>
</header>

<section class="abs hero-main" role="img" aria-label="Food processing worker in hairnet and gloves at a packing line">
  <div class="txt">
    <small>KELMORRA</small>
    <h1>PPE HYGIENE</h1>
    <p>Starting $.99</p>
    <span class="btn btn-white">Shop Now</span>
  </div>
</section>
<aside class="abs promo promo-clear" role="img" aria-label="Clearance products on shelves">
  <h3>Clearance Deals</h3>
  <p>Up to 50% Off</p>
  <span class="btn btn-green">Shop Now</span>
</aside>
<aside class="abs promo promo-drop" role="img" aria-label="Assorted cleaning and safety products">
  <h3>Price Drop</h3>
  <p>Up to 70% Off</p>
  <span class="btn btn-green">Shop Now</span>
</aside>

<section class="abs industry">
  <h2>Shop by Industry</h2><i></i>
  <div class="ind-row">
    <div class="ind"><svg width="56" height="56" viewBox="0 0 56 56" fill="none" stroke="#6aae3c" stroke-width="2.5"><circle cx="28" cy="14" r="7"/><path d="M16 48V32a12 12 0 0 1 24 0v16"/></svg><span>Childcare</span></div>
    <div class="ind"><svg width="56" height="56" viewBox="0 0 56 56" fill="none" stroke="#6aae3c" stroke-width="2.5"><path d="M6 48V24l12 8v-8l12 8v-8l12 8V10h8v38z"/></svg><span>Manufacturing</span></div>
    <div class="ind active"><svg width="56" height="56" viewBox="0 0 56 56" fill="none" stroke="#6aae3c" stroke-width="2.5"><path d="M10 30h36a18 18 0 0 1-36 0z"/><path d="M20 22c0-6 6-6 6-12M30 22c0-6 6-6 6-12"/></svg><span>Food Processing</span></div>
    <div class="ind"><svg width="56" height="56" viewBox="0 0 56 56" fill="none" stroke="#6aae3c" stroke-width="2.5"><circle cx="24" cy="12" r="6"/><path d="M24 20v16h12l4 12M14 30a12 12 0 0 0 22 8"/></svg><span>Aged Care</span></div>
    <div class="ind"><svg width="56" height="56" viewBox="0 0 56 56" fill="none" stroke="#6aae3c" stroke-width="2.5"><path d="M28 10 4 22l24 12 24-12z"/><path d="M14 27v12c8 6 20 6 28 0V27"/></svg><span>Education</span></div>
  </div>
  <span class="btn btn-outline">View All Industry</span>
</section>

<aside class="abs sidebar">
  <div class="side-head">SHOP BY CATEGORY</div>
  <ul class="cat-list">
    <li>PPE Hygiene</li><li>Metal Detectable</li><li>PPE Safety</li><li class="on">Footwear</li><li>Skin Care</li>
    <li>Packaging</li><li>Workwear</li><li>Site Safety</li><li>First Aid</li><li>Janitorial</li>
    <li>Cleaning Equipment</li><li>Cleaning Supplies</li><li>Lunchroom</li><li>Bathroom Products</li><li>Glove Cutting</li>
  </ul>
  <div class="guide">
    <h4>DOWNLOAD</h4>
    <p>BUYER'S GUIDE</p>
    <span class="btn btn-green">Download</span>
    <div class="cover" role="img" aria-label="Buyer's guide booklet cover"></div>
  </div>
</aside>

<section class="abs products">
  <div class="prod-head">FEATURED PRODUCTS</div>
  <div class="grid">
    <article class="card"><div class="thumb" role="img" aria-label="Boxed first aid kit"></div><span class="badge sale">Sale</span>
      <h3>Metal Detectable Blue Plastic Strips – Wide</h3><p class="price"><s>$23.50</s><b>$21.50</b> +GST Per kit</p>
      <div class="opts"><span class="qty">- 1 +</span><span class="stock">In Stock</span></div>
      <div class="actions"><span class="btn btn-outline">Shop Now</span><span class="btn btn-white">Add to Quote</span></div></article>
    <article class="card lift"><div class="thumb alt" role="img" aria-label="First aid kit contents laid out"></div>
      <h3>Metal Detectable Blue Plastic Strips – Wide</h3><p class="price"><s>$23.50</s><b>$21.50</b> +GST Per kit</p>
      <div class="opts"><span class="qty">- 1 +</span><span class="stock">In Stock</span></div>
      <div class="actions"><span class="btn btn-green">Shop Now</span><span class="btn btn-white">Add to Quote</span></div></article>
    <article class="card"><div class="thumb" role="img" aria-label="Boxed first aid kit"></div><span class="badge sale">Sale</span>
      <h3>Metal Detectable Blue Plastic Strips – Wide</h3><p class="price"><s>$23.50</s><b>$21.50</b> +GST Per kit</p>
      <div class="opts"><span class="qty">- 1 +</span><span class="stock">In Stock</span></div>
      <div class="actions"><span class="btn btn-outline">Shop Now</span><span class="btn btn-white">Add to Quote</span></div></article>
    <article class="card"><div class="thumb alt" role="img" aria-label="Open first aid kit with supplies"></div>
      <h3>Metal Detectable Blue Plastic Strips – Wide</h3><p class="price"><s>$23.50</s><b>$21.50</b> +GST Per kit</p>
      <div class="opts"><span class="qty">- 1 +</span><span class="stock">Special Order</span></div>
      <div class="actions"><span class="btn btn-outline">Shop Now</span><span class="btn btn-white">Add to Quote</span></div></article>
    <article class="card"><div class="thumb" role="img" aria-label="Boxed first aid kit"></div><span class="badge new">New</span>
      <h3>Metal Detectable Blue Plastic Strips – Wide</h3><p class="price"><s>$23.50</s><b>$21.50</b> +GST Per kit</p>
      <div class="opts"><span class="qty">- 1 +</span><span class="stock">Special Order</span></div>
      <div class="actions"><span class="btn btn-outline">Shop Now</span><span class="btn btn-white">Add to Quote</span></div></article>
    <article class="card"><div class="thumb alt" role="img" aria-label="First aid kit contents laid out"></div>
      <h3>Metal Detectable Blue Plastic Strips – Wide</h3><p class="price"><s>$23.50</s><b>$21.50</b> +GST Per kit</p>
      <div class="opts"><span class="qty">- 1 +</span><span class="stock">In Stock</span></div>
      <div class="actions"><span class="btn btn-outline">Shop Now</span><span class="btn btn-white">Add to Quote</span></div></article>
  </div>
</section>

<section class="abs suppliers">
  <div class="sup-tag">
    <h2>Our Suppliers</h2>
    <svg width="60" height="120" viewBox="0 0 60 120"><path d="M0 0h30l30 60-30 60H0z" fill="#24282c"/></svg>
  </div>
  <div class="sup-logos"><span>Boxwell</span><span>Clearhand</span><span>Stonegate</span><span>Harbourline</span></div>
</section>

<section class="abs clients">
  <h2>What Our Clients Say</h2><i></i>
  <div class="quote-card">
    <div class="quote-mark">“</div>
    <p>I want to thank the Kelmorra team for their friendly and professional service. After conversations with your sales team, I'm always left confident that my request is in good hands. I will continue to support Kelmorra and look forward to our dealings in the future.</p>
    <p class="who"><b>Brendan</b> – Education Industry</p>
  </div>
</section>

<section class="abs news">
  <h2>Latest News</h2><i></i>
  <div class="news-grid">
    <article class="news-card"><div class="news-img n1" role="img" aria-label="Product labels on packaged goods"></div><p class="cat">RESEARCH</p><h3>Beware! the mislabelling errors that can lead to costly recalls</h3></article>
    <article class="news-card"><div class="news-img n2" role="img" aria-label="Blue crates on a production floor"></div><p class="cat">RESEARCH</p><h3>Two quick wins to make productivity gains at work</h3></article>
    <article class="news-card"><div class="news-img n3" role="img" aria-label="Bread production line in a bakery"></div><p class="cat">RESEARCH</p><h3>The massive bread recall that could have been avoided ...</h3></article>
  </div>
  <span class="btn btn-outline">View All News</span>
</section>

<footer class="abs site-footer">
  <div class="fcol" style="left:72px;width:300px">
    <h4>Stay Connected</h4>
    <p>Sign up for our news, deals and new product updates for every industry.</p>
    <div class="subscribe"><span>Enter email</span><b>Sign Up</b></div>
    <div class="socials"><i></i><i></i></div>
  </div>
  <div class="fcol contact" style="left:470px;width:300px">
    <h4>Kelmorra</h4>
    <p>Local supplier of hygiene, safety and cleaning products across Victoria.</p>
    <ul style="margin-top:10px">
      <li><svg width="12" height="12" viewBox="0 0 12 12" fill="#6aae3c"><path d="M2 1h3l1 3-2 1a7 7 0 0 0 3 3l1-2 3 1v3c-6 1-10-3-9-9z"/></svg>1800 555 214</li>
      <li><svg width="12" height="12" viewBox="0 0 12 12" fill="none" stroke="#6aae3c"><rect x="1" y="2.5" width="10" height="7"/><path d="m1 3 5 4 5-4"/></svg>sales@kelmorra.com.au</li>
      <li><svg width="12" height="12" viewBox="0 0 12 12" fill="#6aae3c"><path d="M6 0a4 4 0 0 1 4 4c0 3-4 8-4 8S2 7 2 4a4 4 0 0 1 4-4z"/></svg>12 Wattle Court, Dandenong VIC 3175</li>
    </ul>
  </div>
  <div class="fcol" style="left:868px;width:260px">
    <h4>Site Links</h4>
    <div class="links"><span>Home</span><span>Newsletters</span><span>About Us</span><span>Industries</span><span>Contact Kelmorra</span><span>Contact Us</span><span>Returns Policy</span><span>Supplier Area</span><span>Privacy Policy</span></div>
  </div>
  <div class="copy"><span>© 2024 Kelmorra. All Rights Reserved.</span><span>Privacy · Terms of Use</span></div>
</footer>

</body>
</html>
```